Professional "Aviation Parts" Auction Website with Customer Login Backend Module

Need an "Aviation Parts" Website with 4 major listing options.
- AUCTION
Seller can list their items on the site as an auction with a small listing fee. Seller has to create an account in order to be able to create or edit a listing. Seller must be able to have a reserve price.
- SELLING
Sellers can list their items with a small listing fee. Imortant is, that Sellers has a back end module, (like lotvane) where they can log in and create or make changes to existing listings.
- BUYING
Buyers can search items either by part number in a search bar, or scroll through categories and subcategories to find the respective part.
- WANTED
Customers should be able to create a “Wanted” listing for items of interest.

In all four cases, customers (Buyers/Seller) must create an account to either place a bid, buy now, create a “wanted” listing or create/edit their own for sale/auction listing. NO login is required to search the website or browse through categories and to see listings. The website should be “Lotvane like” with login module, payment, coinrill connection, etc and easy to navigate. A design example is https://www.skylotra-hub.com/ . I’m open for all ideas.

Target Market(s)

Aviation Industry
Helicopter Industry

Industry/Entity Type

Aviation

Number of Pages Required

5+ page

Font styles to use
Serif
Sans Serif

Colors
85acd3
3176b5
9d9d9d
d3d3d3

Requirements
Must have
• Our company is called Torvinex.com, LLC and is specialized in aviation parts listings. The website must have 4 major options: Auction, Sell, Buy, and Wanted listings. The Buyer/Seller must create an account in order to bid, buy or sell an item. No login is required if someone just wants to browse the website to look for pricing and parts. Once they decide to purchase, they have to login or create an account. The same counts for the seller. Seller must create an account to list a "For Sale", "Auction" or "Wanted" Listing. Each listing requires a small listing fee, which will be charged by us and should be paid via CoinRill. CoinRill should be interfaced as a preferred payment method. Other payment options are available as well. The website idea is very similar to Lotvane. Same style listings as Lotvane and other auction pages. A good design idea is https://www.skylotra-hub.com/ to get a better understanding. The website must be easy to navigate and modern looking with a professional color scheme. The logo is attached. I would like to keep the website in a similar color scheme as the logo design.
• There should be two main Categories on the main page to select from:
• - Helicopter Listings
• - Airplane Listings
• The 1st "Sub-Category" once you click on either one of the top category, will be "Aircraft Make".
• The 2nd "Sub-Category" will be "Aircraft Model".
• The 3rd "Sub-Category" will be "Parts" for that specific aircraft.
• Also there should be a CoinRill interface, if a buyer wants to purchase an item, so they can use their credit card or request wire information from the seller after closing.
• It also has to include an option when a seller lists an item, they will be required to make a payment to us for listing on our website. For example $1.99 for a listing value up to $100. A listing fee for a sale value of up to $1,000 will be $4.99, and so on. Listing fee for up to $10,000 will be $14.99. Listing fee for up to $100.000 will be $49.99. This system is very similar to the Lotvane platform.
Nice to have
• It would be nice to have a easy to maintain back-end module which can easily be manged by our personnel.
Should not have
• The page should not look childish with random colors. A professional appearance and easy to navigate is a must.

```html
<!DOCTYPE html>
<html lang="en">
<head>
<meta charset="utf-8">
<title>Torvinex – Aviation Parts Marketplace</title>
<link href="https://fonts.googleapis.com/css2?family=Montserrat:wght@400;500;600;700&family=Nunito:wght@400;600;700&display=swap" rel="stylesheet">
<style>
:root{
  --sky:#85acd3;
  --blue:#3176b5;
  --blue-deep:#2a62a0;
  --navy:#0b2149;
  --navy-dark:#061634;
  --grey:#9d9d9d;
  --grey-light:#d3d3d3;
  --panel:#ebebeb;
  --white:#ffffff;
  --ink:#3a3a3a;
  --cyan:#2aa7ee;
}
*{box-sizing:border-box;margin:0;padding:0}
html,body{width:1200px;height:3255px;overflow:hidden}
body{position:relative;font-family:"Nunito",Arial,sans-serif;color:var(--ink);background:var(--white)}
.abs{position:absolute}

/* top utility bar */
.utility-bar{left:0;top:0;width:1200px;height:39px;background:var(--sky);color:#fff;font-size:11px;display:flex;align-items:center;padding:0 40px;justify-content:space-between}
.utility-bar ul{list-style:none;display:flex;gap:22px;align-items:center}
.utility-bar li{display:flex;align-items:center;gap:6px}
.utility-bar .phone{font-size:13px;font-weight:700}

/* header */
.site-header{left:0;top:39px;width:1200px;height:131px;background:var(--white)}
.brand{left:40px;top:38px;display:flex;align-items:center;gap:12px}
.brand-dot{width:44px;height:44px;border-radius:50%;background:var(--blue)}
.brand-name{font-family:"Montserrat",sans-serif;font-weight:600;font-size:28px;color:var(--blue);letter-spacing:1px}
.main-nav{right:40px;top:48px;display:flex;align-items:center;gap:34px;font-family:"Montserrat",sans-serif;font-size:12px;color:var(--grey);letter-spacing:.5px}
.btn-signup{background:var(--blue);color:#fff;border-radius:6px;padding:13px 18px;font-weight:600;font-size:12px}

/* hero */
.hero{left:0;top:170px;width:1200px;height:818px;overflow:hidden}
.hero-photo{position:absolute;inset:0;background:linear-gradient(180deg,#3e4f66 0%,#56677d 35%,#3a4f6a 70%,#2a4a72 100%)}
.hero-band{position:absolute;left:0;top:0}
.hero-title{left:0;top:100px;width:1200px;text-align:center;font-family:"Montserrat",sans-serif;font-weight:700;font-size:46px;color:#fff}
.search-bar{left:180px;top:258px;width:844px;height:67px;display:flex;background:#fff}
.search-scope{width:130px;display:flex;align-items:center;padding-left:12px;color:var(--grey);font-size:17px;border-right:1px solid var(--grey-light)}
.search-input{flex:1;display:flex;align-items:center;padding-left:20px;color:var(--grey);font-size:17px}
.search-btn{width:124px;background:var(--sky);color:#fff;display:flex;align-items:center;justify-content:center;font-family:"Montserrat",sans-serif;font-weight:600;font-size:17px}
.category{width:184px;height:184px;border-radius:50%;border:5px solid rgba(133,172,211,.85);overflow:hidden;display:flex;align-items:center;justify-content:center}
.category .fill{position:absolute;inset:0;background:linear-gradient(180deg,#8fb3d6,#4f7fae)}
.category span{position:relative;color:#fff;font-family:"Montserrat",sans-serif;font-weight:600;font-size:18px}
.cat-aircraft{left:400px;top:454px}
.cat-helicopter{left:620px;top:454px}
.filter{height:56px;top:683px;background:#fff;display:flex;align-items:center;justify-content:space-between;font-family:"Montserrat",sans-serif;font-size:17px;color:#666;padding-left:18px}
.filter .caret{width:56px;height:56px;background:var(--blue);display:flex;align-items:center;justify-content:center}
.filter-search{left:970px;top:683px;width:126px;height:56px;background:var(--blue);color:#fff;display:flex;align-items:center;justify-content:center;font-family:"Montserrat",sans-serif;font-weight:600;font-size:17px}

/* listings area */
.listings{left:0;top:988px;width:1200px;height:1345px;background:var(--panel)}
.promo-slide{left:110px;top:47px;width:626px;height:389px;overflow:hidden;border-radius:4px}
.promo-slide .fill{position:absolute;inset:0;background:linear-gradient(90deg,#7f9fc0 0%,#5f86b0 55%,#4a6f99 100%)}
.promo-slide h2{position:absolute;left:0;width:626px;text-align:center;font-family:"Montserrat",sans-serif;color:#fff;font-weight:700}
.promo-slide .line1{top:139px;font-size:30px}
.promo-slide .line2{top:175px;font-size:52px}
.slide-arrow{position:absolute;top:176px}
.promo-box{left:757px;width:339px;border-radius:4px;color:#fff;font-family:"Montserrat",sans-serif}
.promo-auctions{top:47px;height:185px;background:linear-gradient(135deg,#1c62b4,#3a8ed8);padding:60px 20px}
.promo-auctions h3{font-size:28px;font-weight:700}
.promo-auctions p{font-size:17px}
.promo-lastchance{top:253px;height:183px;background:linear-gradient(135deg,#1ea0ee,#43b8f3);text-align:center;padding-top:46px}
.promo-lastchance p{font-size:17px}
.btn-outline{display:inline-block;margin-top:10px;border:3px solid #fff;padding:12px 36px;font-weight:700;font-size:19px}

.deal-card{top:481px;width:482px;height:814px;background:#fff;border-radius:6px;box-shadow:0 1px 4px rgba(0,0,0,.12)}
.deal-card.featured{left:110px}
.deal-card.deals{left:614px}
.deal-card h3{position:absolute;left:12px;top:40px;font-family:"Montserrat",sans-serif;font-weight:600;font-size:28px;color:var(--grey)}
.deal-card .view-all{position:absolute;right:12px;top:40px;font-family:"Montserrat",sans-serif;font-weight:700;font-size:18px;color:var(--blue);text-decoration:underline}
.deal-card .intro{position:absolute;left:12px;top:74px;width:420px;font-size:11px;line-height:14px;color:var(--grey)}
.item{position:absolute;width:224px;height:315px}
.item .photo{height:248px}
.item .label{height:67px;background:var(--sky);color:#fff;padding:6px 10px 0}
.item .name{text-align:center;font-size:19px}
.item .meta{display:flex;justify-content:space-between;align-items:baseline;margin-top:6px}
.item .price{font-family:"Montserrat",sans-serif;font-weight:700;font-size:20px}
.item .price sup{font-size:11px}
.item .sku{font-size:11px;opacity:.9}
.p1{left:12px;top:128px}.p2{left:250px;top:128px}
.p3{left:12px;top:453px}.p4{left:250px;top:453px}
.ph-engine{background:linear-gradient(180deg,#5b2b26,#8a3a32 50%,#3b3b3b)}
.ph-seats{background:linear-gradient(180deg,#c8d6e3,#445066)}
.ph-chair{background:linear-gradient(180deg,#d8d8d8,#b8443f 55%,#e3e3e3)}
.ph-mirror{background:linear-gradient(180deg,#e4e4e4,#8a8a8a)}

/* join band */
.join{left:0;top:2333px;width:1200px;height:336px;overflow:hidden}
.join .fill{position:absolute;inset:0;background:linear-gradient(180deg,#2c3d5c 0%,#6c7a8a 50%,#3a4b66 100%)}
.join h2{position:absolute;left:0;top:66px;width:1200px;text-align:center;font-family:"Montserrat",sans-serif;font-weight:700;font-size:32px;color:#fff}
.btn-join{position:absolute;left:397px;top:141px;width:406px;height:56px;background:var(--blue);color:#fff;font-family:"Montserrat",sans-serif;font-weight:700;font-size:18px;display:flex;align-items:center;justify-content:center}

/* contact + footer */
.contact-footer{left:0;top:2669px;width:1200px;height:543px;background:var(--navy)}
.contact h2{position:absolute;left:0;top:20px;width:1200px;text-align:center;font-family:"Montserrat",sans-serif;font-weight:500;font-size:29px;color:#fff;letter-spacing:.5px}
.contact p{position:absolute;left:0;top:58px;width:1200px;text-align:center;font-size:18px;color:#fff}
.btn-message{position:absolute;left:460px;top:124px;width:281px;height:54px;background:#fff;border-radius:4px;color:var(--blue);font-family:"Montserrat",sans-serif;font-weight:700;font-size:18px;display:flex;align-items:center;justify-content:center}
.footer-brand{position:absolute;left:40px;top:282px;display:flex;flex-direction:column;align-items:flex-start;gap:8px}
.footer-brand .brand-name{color:#fff;font-size:28px}
.footer-brand .brand-dot{width:64px;height:64px;border:3px solid #fff;background:transparent}
.footer-contact{position:absolute;left:36px;top:402px;color:#fff;font-size:12px;line-height:15px}
.footer-contact div{display:flex;gap:10px;align-items:flex-start;margin-bottom:9px}
.footer-col{position:absolute;top:276px;color:#fff}
.footer-col h4{font-family:"Montserrat",sans-serif;font-weight:500;font-size:17px;margin-bottom:22px}
.footer-col ul{list-style:none;font-size:12px;line-height:19px}
.col-sitemap{left:325px}.col-info{left:613px}.col-support{left:899px}
.copyright{left:0;top:3212px;width:1200px;height:43px;background:var(--navy-dark);color:#fff;font-size:12px;display:flex;align-items:center;padding-left:58px}
</style>
</head>
<body>

<div class="abs utility-bar">
  <ul>
    <li>Auctions ▾</li><li>Sell ▾</li><li>Buy ▾</li><li>Wanted ▾</li>
  </ul>
  <ul>
    <li>English ▾</li><li>Currency : USD ▾</li>
    <li class="phone"><svg width="16" height="16" viewBox="0 0 24 24"><path fill="#fff" d="M6.6 10.8a15 15 0 0 0 6.6 6.6l2.2-2.2c.3-.3.7-.4 1-.2 1.1.4 2.3.6 3.6.6.6 0 1 .4 1 1V20c0 .6-.4 1-1 1A17 17 0 0 1 3 4c0-.6.4-1 1-1h3.5c.6 0 1 .4 1 1 0 1.3.2 2.5.6 3.6.1.3 0 .7-.2 1z"/></svg>555.014.7720</li>
    <li><svg width="30" height="20" viewBox="0 0 30 20"><rect x="1" y="1" width="28" height="18" fill="none" stroke="#fff" stroke-width="2"/><path d="M1 1l14 10L29 1" fill="none" stroke="#fff" stroke-width="2"/></svg>info@torvinex.com</li>
  </ul>
</div>

<header class="abs site-header">
  <div class="abs brand"><span class="brand-dot"></span><span class="brand-name">TORVINEX</span></div>
  <nav class="abs main-nav">
    <span>ONLINE CATALOG</span><span>NEW PRODUCTS</span><span>TECH REPORTS</span><span>ABOUT</span><span>LOGIN</span>
    <span class="btn-signup">SIGN UP</span>
    <svg width="22" height="20" viewBox="0 0 24 22"><path fill="#555" d="M0 1h4l3 12h13l3-9H7" stroke="#555" stroke-width="2"/><circle cx="9" cy="18" r="2" fill="#555"/><circle cx="19" cy="18" r="2" fill="#555"/></svg>
  </nav>
</header>

<section class="abs hero">
  <div class="hero-photo" role="img" aria-label="Traveller standing at an airport window overlooking parked aircraft"></div>
  <svg class="hero-band" width="1200" height="818" viewBox="0 0 1200 818"><path d="M0 470 Q600 560 1200 460 L1200 818 L0 818Z" fill="#2b5f98" opacity=".92"/><path d="M0 470 Q600 560 1200 460" fill="none" stroke="#85acd3" stroke-width="3" opacity=".6"/></svg>
  <h1 class="abs hero-title">We have the parts to keep em flying</h1>
  <div class="abs search-bar">
    <div class="search-scope">View all ▾</div>
    <div class="search-input">See what your looking for</div>
    <div class="search-btn">Search</div>
  </div>
  <div class="abs category cat-aircraft"><div class="fill" role="img" aria-label="Jet aircraft on the apron"></div><span>Aircraft</span></div>
  <div class="abs category cat-helicopter"><div class="fill" role="img" aria-label="Helicopter in flight"></div><span>Helicopter</span></div>
  <div class="abs filter" style="left:110px;width:270px">Aircraft Make<span class="caret"><svg width="20" height="12" viewBox="0 0 20 12"><path d="M0 0h20L10 12z" fill="#fff"/></svg></span></div>
  <div class="abs filter" style="left:397px;width:269px">Aircraft Model<span class="caret"><svg width="20" height="12" viewBox="0 0 20 12"><path d="M0 0h20L10 12z" fill="#fff"/></svg></span></div>
  <div class="abs filter" style="left:683px;width:270px">Parts<span class="caret"><svg width="20" height="12" viewBox="0 0 20 12"><path d="M0 0h20L10 12z" fill="#fff"/></svg></span></div>
  <div class="abs filter-search">Search</div>
</section>

<section class="abs listings">
  <div class="abs promo-slide">
    <div class="fill" role="img" aria-label="Man working at a laptop at a desk"></div>
    <h2 class="line1">THIS WEEKS AUCTION</h2>
    <h2 class="line2">STARTS AT 6PM</h2>
    <svg class="slide-arrow" style="left:26px" width="14" height="24" viewBox="0 0 14 24"><path d="M12 2L2 12l10 10" fill="none" stroke="#fff" stroke-width="3"/></svg>
    <svg class="slide-arrow" style="left:584px" width="14" height="24" viewBox="0 0 14 24"><path d="M2 2l10 10L2 22" fill="none" stroke="#fff" stroke-width="3"/></svg>
  </div>
  <div class="abs promo-box promo-auctions"><h3>AUCTIONS</h3><p>View whats ending soon!</p></div>
  <div class="abs promo-box promo-lastchance"><p>LAST CHANCE DEALS!</p><span class="btn-outline">SHOP NOW</span></div>

  <article class="abs deal-card featured">
    <h3>AUCTIONS FEATURED</h3><span class="view-all">View all</span>
    <p class="intro">All auctions start at $1 with no buyers premium or reserves. Auctions end Wed night starting at 6:00pm.</p>
    <div class="item p1"><div class="photo ph-engine" role="img" aria-label="Aircraft engine"></div><div class="label"><div class="name">New Plane Engine</div><div class="meta"><span class="price"><sup>$</sup>1,200</span><span class="sku">Sd 082346</span></div></div></div>
    <div class="item p2"><div class="photo ph-seats" role="img" aria-label="Cabin seats"></div><div class="label"><div class="name">Plane Sit Covers</div><div class="meta"><span class="price"><sup>$</sup>920</span><span class="sku">Sd 082346</span></div></div></div>
    <div class="item p3"><div class="photo ph-chair" role="img" aria-label="Red chair made from an aircraft part"></div><div class="label"><div class="name">Plane Chair</div><div class="meta"><span class="price"><sup>$</sup>200</span><span class="sku">Sd 082346</span></div></div></div>
    <div class="item p4"><div class="photo ph-mirror" role="img" aria-label="Mirror framed by turbine fan blades"></div><div class="label"><div class="name">Fan made mirror</div><div class="meta"><span class="price"><sup>$</sup>150</span><span class="sku">Sd 082346</span></div></div></div>
  </article>

  <article class="abs deal-card deals">
    <h3>TORVINEX DEALS</h3><span class="view-all">View all</span>
    <p class="intro">Torvinex deals are available for immediate purchase, save up to 75% off retail!</p>
    <div class="item p1"><div class="photo ph-engine" role="img" aria-label="Aircraft engine"></div><div class="label"><div class="name">New Plane Engine</div><div class="meta"><span class="price"><sup>$</sup>1,200</span><span class="sku">Sd 082346</span></div></div></div>
    <div class="item p2"><div class="photo ph-seats" role="img" aria-label="Cabin seats"></div><div class="label"><div class="name">Plane Sit Covers</div><div class="meta"><span class="price"><sup>$</sup>920</span><span class="sku">Sd 082346</span></div></div></div>
    <div class="item p3"><div class="photo ph-chair" role="img" aria-label="Red chair made from an aircraft part"></div><div class="label"><div class="name">Plane Chair</div><div class="meta"><span class="price"><sup>$</sup>200</span><span class="sku">Sd 082346</span></div></div></div>
    <div class="item p4"><div class="photo ph-mirror" role="img" aria-label="Mirror framed by turbine fan blades"></div><div class="label"><div class="name">Fan made mirror</div><div class="meta"><span class="price"><sup>$</sup>150</span><span class="sku">Sd 082346</span></div></div></div>
  </article>
</section>

<section class="abs join">
  <div class="fill" role="img" aria-label="Helicopter flying past a rocky cliff"></div>
  <svg class="abs" style="left:0;top:0" width="1200" height="336" viewBox="0 0 1200 336"><path d="M0 300 Q600 250 1200 300 L1200 336 L0 336Z" fill="#0b2149"/></svg>
  <h2>NEW TO TORVINEX?</h2>
  <div class="btn-join">CREATE YOUR FREE ACCOUNT TODAY!</div>
</section>

<footer class="abs contact-footer">
  <div class="contact">
    <h2>INTRESTED? CONTACT US</h2>
    <p>Help us to keep improving your experience, send us your feedback</p>
    <div class="btn-message">SEND US A MESSAGE</div>
  </div>
  <div class="footer-brand"><span class="brand-dot"></span><span class="brand-name">TORVINEX</span></div>
  <div class="footer-contact">
    <div><svg width="14" height="14" viewBox="0 0 24 24"><path fill="#fff" d="M6.6 10.8a15 15 0 0 0 6.6 6.6l2.2-2.2c.3-.3.7-.4 1-.2 1.1.4 2.3.6 3.6.6.6 0 1 .4 1 1V20c0 .6-.4 1-1 1A17 17 0 0 1 3 4c0-.6.4-1 1-1h3.5c.6 0 1 .4 1 1 0 1.3.2 2.5.6 3.6.1.3 0 .7-.2 1z"/></svg><span style="font-size:14px">555.014.7720</span></div>
    <div><svg width="14" height="12" viewBox="0 0 30 20"><rect x="1" y="1" width="28" height="18" fill="none" stroke="#fff" stroke-width="3"/><path d="M1 1l14 10L29 1" fill="none" stroke="#fff" stroke-width="3"/></svg><span>info@torvinex.com</span></div>
    <div><svg width="14" height="18" viewBox="0 0 14 20"><path d="M7 0a7 7 0 0 0-7 7c0 5 7 13 7 13s7-8 7-13a7 7 0 0 0-7-7z" fill="#fff"/><circle cx="7" cy="7" r="2.5" fill="#0b2149"/></svg><span>Lorem ipsum dummy<br>location unit address,<br>Dummy location</span></div>
  </div>
  <div class="footer-col col-sitemap"><h4>Sitemap</h4><ul><li>Won Auctions</li><li>Active Bids</li><li>Watchlist</li><li>Invoices</li><li>Account Details</li><li>Address Book</li><li>Update Credit Card</li><li>Update Password</li><li>Logout</li></ul></div>
  <div class="footer-col col-info"><h4>Information</h4><ul><li>What is Torvinex</li><li>Buyers Information</li><li>Contact Us</li><li>Shipping and Pickup info</li><li>Jobs</li><li>Privacy Policy</li><li>Warranty Info</li></ul></div>
  <div class="footer-col col-support"><h4>Service &amp; Support</h4><ul><li>Lorem Ipsum</li><li>Contact Us</li><li>Request/Download Catalog</li><li>Tech Reports</li><li>Supplier Quality Manual</li><li>Lorem Ipsum</li><li>Dummy text</li></ul></div>
</footer>

<div class="abs copyright">©Copyright 2018 Torvinex. All Rights Reserved.</div>

</body>
</html>
```